Sale of South Sea and Tahitian Pearl Jewellery, online business

I need a business card designed for my website business. We sell South Sea and Tahitian Pearl Jewellery. The colour theme for the website is black and white and would like to carry this through to business cards. Our brand is very elegant and stylish, would like sketch picture of women or fashion involving pearls if not the sketched picture then have the card very plan. below are pictures of the ideas I like and also the logo and writing that is used on my jewellery boxes.
Font is English Hand DB

Target Market(s)

30 and over women in the high end of the market

Industry/Entity Type

Business

Contact Information for Business Card

Business name - Varno Gems( front of card)
Back of card -Details
Rosalind Thackery
Gemmologist MDRS
email: rosalind@varnogems.com.au
website: varnogems.com.au
mob: +61 427 508 193
Corrin Bay Australia

Varno Stelle PTY T/AS Varno Gems
ABN 47 283 915 604

Colors
1b1b1b
ffffff
85cae6

Requirements
Must have
• Black and white colour preferably black card with white writing and picture.
• The Same writing as logo and writing on box packaging, attached a file with writing.
• Business name on one side of the card and all other details on the other side.
• Can have tiny hints of the harbour blue colour.
• Font: English Hand DB
Nice to have
• I really like the idea of having a sketch of a stylish or elegent lady wearing pearls or a sketch of a pearl, if not the sketch a really plain and simple card.
Should not have
• busy patterns.

```html
<!DOCTYPE html>
<html lang="en">
<head>
<meta charset="utf-8">
<title>Varno Gems — Business Card</title>
<link rel="stylesheet" href="https://fonts.googleapis.com/css2?family=Pinyon+Script&family=Arimo:wght@400;700&display=swap">
<style>
  :root {
    --ink: #1b1b1b;
    --paper: #ffffff;
    --black-card: #000000;
    --backdrop-edge: #2e2e2e;
    --backdrop-mid: #5a5a5a;
    --ornament-light: #e9e9e9;
    --ornament-dark: #2a2a2a;
  }
  html, body {
    margin: 0;
    padding: 0;
    width: 999px;
    height: 1200px;
    overflow: hidden;
  }
  .presentation {
    position: relative;
    width: 999px;
    height: 1200px;
    background: radial-gradient(ellipse at center, var(--backdrop-mid) 0%, #4a4a4a 55%, var(--backdrop-edge) 100%);
    font-family: "Arimo", Arial, sans-serif;
  }
  .card {
    position: absolute;
    left: 42px;
    width: 915px;
    height: 522px;
    overflow: hidden;
  }
  .card--front { top: 57px; background: var(--paper); color: var(--ink); }
  .card--back { top: 621px; background: var(--black-card); color: var(--paper); }

  .brand-name {
    position: absolute;
    left: 30px;
    top: 80px;
    margin: 0;
    font-family: "Pinyon Script", cursive;
    font-weight: 400;
    font-size: 82px;
    line-height: 1;
    color: var(--ink);
  }
  .holder-name {
    position: absolute;
    left: 33px;
    top: 278px;
    margin: 0;
    font-family: "Pinyon Script", cursive;
    font-weight: 400;
    font-size: 50px;
    line-height: 1;
    color: var(--ink);
    -webkit-text-stroke: 0.6px var(--ink);
  }
  .holder-title {
    position: absolute;
    left: 31px;
    top: 341px;
    margin: 0;
    font-size: 22px;
    color: var(--ink);
  }
  .contact-list {
    position: absolute;
    left: 31px;
    top: 408px;
    margin: 0;
    padding: 0;
    list-style: none;
    font-size: 24px;
    line-height: 31px;
  }
  .contact-list li { display: flex; align-items: center; white-space: nowrap; }
  .contact-icon { width: 18px; height: 18px; margin: 0 22px 0 2px; flex: none; }
  .company-block {
    position: absolute;
    left: 519px;
    top: 408px;
    margin: 0;
    font-size: 23px;
    line-height: 31px;
    font-style: normal;
    white-space: nowrap;
  }
  .company-block strong { font-weight: 700; }

  .ornament { position: absolute; border-radius: 6px; }
  .ornament--front-corner {
    left: 603px; top: 33px; width: 282px; height: 287px;
    background: linear-gradient(135deg, var(--ornament-light), #f6f6f6);
  }
  .ornament--back-top {
    left: 631px; top: 29px; width: 254px; height: 256px;
    background: linear-gradient(135deg, var(--ornament-dark), #151515);
  }
  .ornament--back-bottom {
    left: 30px; top: 239px; width: 255px; height: 256px;
    background: linear-gradient(315deg, var(--ornament-dark), #151515);
  }

  .seal {
    position: absolute;
    left: 307px;
    top: 109px;
    width: 304px;
    height: 304px;
    box-sizing: border-box;
    border: 4px solid var(--paper);
    border-radius: 50%;
    display: flex;
    align-items: center;
    justify-content: center;
  }
  .seal-name {
    margin: 0;
    font-family: "Pinyon Script", cursive;
    font-weight: 400;
    font-size: 46px;
    color: var(--paper);
  }
</style>
</head>
<body>
<main class="presentation">

  <section class="card card--front" aria-label="Card front">
    <h1 class="brand-name">Varno Gems</h1>
    <div class="ornament ornament--front-corner" role="img" aria-label="Black swirling filigree flourish in the top right corner"></div>

    <p class="holder-name">Rosalind Thackery</p>
    <p class="holder-title">Gemmologist MDRS</p>

    <ul class="contact-list">
      <li>
        <svg class="contact-icon" viewBox="0 0 18 18" aria-hidden="true">
          <rect x="4" y="1" width="10" height="16" rx="2" fill="var(--ink)"/>
          <rect x="6" y="3.5" width="6" height="9" fill="var(--paper)"/>
        </svg>
        +61 427 508 193
      </li>
      <li>
        <svg class="contact-icon" viewBox="0 0 18 18" aria-hidden="true">
          <path d="M1 7 L9 2 L17 7 V16 H1 Z" fill="var(--ink)"/>
          <path d="M3 8 L9 12 L15 8" stroke="var(--paper)" stroke-width="1.6" fill="none"/>
        </svg>
        rosalind@varnogems.com.au
      </li>
      <li>
        <svg class="contact-icon" viewBox="0 0 18 18" aria-hidden="true" fill="none" stroke="var(--ink)" stroke-width="1.2">
          <circle cx="9" cy="9" r="7.5"/>
          <ellipse cx="9" cy="9" rx="3.3" ry="7.5"/>
          <line x1="1.5" y1="9" x2="16.5" y2="9"/>
          <line x1="2.8" y1="5" x2="15.2" y2="5"/>
          <line x1="2.8" y1="13" x2="15.2" y2="13"/>
        </svg>
        varnogems.com.au
      </li>
    </ul>

    <address class="company-block">
      <strong>Corrin Bay Australia</strong><br>
      Varno Stelle PTY T/AS Varno Gems<br>
      <strong>ABN</strong> 47 283 915 604
    </address>
  </section>

  <section class="card card--back" aria-label="Card back">
    <div class="ornament ornament--back-top" role="img" aria-label="White swirling filigree flourish in the top right corner"></div>
    <div class="seal">
      <p class="seal-name">Varno Gems</p>
    </div>
    <div class="ornament ornament--back-bottom" role="img" aria-label="White swirling filigree flourish in the bottom left corner"></div>
  </section>

</main>
</body>
</html>
```